Need a stunning looking Business Card Design for my Telecom Business, Wow FACTOR!

I deal with high level IT Directors , and Contractors.
I need to impress them with a sleek , professional and unique business card.
Im thinking options as far as rounded edges, plastic , or even metal card or die cut on a corner.
Whatever looks better and leave an unforgettable first impression.
im looking for the wow factor.
Front should have the basics info (attached on the picture of current business card)
i would like to add picture of myself somewhere
Back side
should have logo and maybe some pictures or past projects, you can download from my website ( www.lumvexholdings.com)

```html
<!DOCTYPE html>
<html lang="en">
<head>
<meta charset="utf-8">
<title>Lumvex Holdings — Business Card</title>
<link rel="stylesheet" href="https://fonts.googleapis.com/css2?family=Saira:wght@400;500;700;800&family=Saira+Semi+Condensed:wght@400;500&display=swap">
<style>
  :root {
    --bg: #2a2b2e;
    --navy: #16235a;
    --navy-deep: #111c4b;
    --paper: #ffffff;
    --cyan: #3fb6e6;
    --gold: #f2b705;
    --green: #7bbf2a;
    --line: #6f9a2f;
    --ink: #ffffff;
    --ink-dark: #1a2240;
    --ring: #e9ecf1;
  }
  * { box-sizing: border-box; margin: 0; padding: 0; }
  html, body { width: 1200px; height: 900px; overflow: hidden; background: var(--bg); }
  .canvas { position: relative; width: 1200px; height: 900px; }

  .card {
    position: absolute;
    width: 350px;
    height: 620px;
    border-radius: 34px;
    overflow: hidden;
    box-shadow: 0 14px 30px rgba(0,0,0,.45);
  }
  .card--front { left: 215px; top: 140px; background: var(--navy); }
  .card--back  { left: 635px; top: 140px; background: linear-gradient(160deg, var(--navy) 0%, var(--navy-deep) 100%); }

  .front-top { position: absolute; inset: 0; }

  .wordmark {
    position: absolute;
    left: 0; right: 0;
    display: flex; align-items: center; justify-content: center; gap: 10px;
    font-family: "Saira", sans-serif;
    font-weight: 500;
    letter-spacing: 1px;
    white-space: nowrap;
  }
  .wordmark__dot { width: 16px; height: 16px; border-radius: 50%; background: var(--cyan); flex: none; }
  .wordmark--front { top: 90px; font-size: 25px; color: var(--ink-dark); }
  .wordmark--back { top: 480px; left: 40px; right: 10px; font-size: 25px; color: var(--ink); }

  .portrait-ring {
    position: absolute; left: 91px; top: 138px;
    width: 168px; height: 168px; border-radius: 50%;
    background: var(--ring);
    display: flex; align-items: center; justify-content: center;
  }
  .portrait {
    width: 140px; height: 140px; border-radius: 50%;
    border: 3px solid #3b5f9e;
    background: radial-gradient(circle at 45% 40%, #c9a487 0%, #9d8e86 45%, #6e7884 100%);
  }

  .person { position: absolute; left: 0; right: 0; top: 312px; text-align: center; }
  .person__name {
    font-family: "Saira", sans-serif; font-weight: 800;
    font-size: 25px; line-height: 30px; letter-spacing: 2px; color: var(--cyan);
  }
  .person__role {
    font-family: "Saira Semi Condensed", sans-serif; font-weight: 500;
    font-size: 18px; line-height: 22px; letter-spacing: 1px; color: var(--gold);
  }

  .divider { position: absolute; left: 40px; right: 40px; height: 1px; background: var(--line); }

  .icon-row { position: absolute; left: 0; right: 0; display: flex; justify-content: center; gap: 10px; }
  .icon { width: 22px; height: 22px; }

  .contact {
    position: absolute; left: 0; right: 0; text-align: center;
    font-family: "Saira Semi Condensed", sans-serif; font-size: 15px;
    color: var(--ink); line-height: 21px; letter-spacing: .5px;
    white-space: nowrap;
  }
  .contact--offices { font-size: 14px; }

  .back-url {
    position: absolute; left: 20px; top: 32px;
    writing-mode: vertical-rl;
    font-family: "Saira", sans-serif; font-weight: 500;
    font-size: 22px; letter-spacing: 4px; color: var(--cyan);
  }
</style>
</head>
<body>
<main class="canvas">

  <section class="card card--front" aria-label="Business card front">
    <svg class="front-top" width="350" height="620" viewBox="0 0 350 620" aria-hidden="true">
      <path d="M0 0 H350 V150 L0 250 Z" fill="var(--paper)"/>
    </svg>

    <div class="wordmark wordmark--front">
      <span class="wordmark__dot"></span><span>LUMVEX HOLDINGS</span>
    </div>

    <div class="portrait-ring">
      <div class="portrait" role="img" aria-label="Portrait photo of Kenji Arlo"></div>
    </div>

    <div class="person">
      <div class="person__name">KENJI ARLO</div>
      <div class="person__role">Operations Manager</div>
    </div>

    <div class="divider" style="top:380px"></div>
    <div class="icon-row" style="top:369px">
      <svg class="icon" viewBox="0 0 24 24" aria-label="Phone">
        <circle cx="12" cy="12" r="12" fill="var(--green)"/>
        <path d="M7 10c0-2 2-3 5-3s5 1 5 3l-2 1-1-2h-4l-1 2z M8 12h8l1 5H7z" fill="var(--navy)"/>
      </svg>
    </div>
    <div class="contact" style="top:398px">
      (410) 555-0147 Harborview<br>
      (620) 555-0182 Northgate<br>
      (731) 555-0136 Lakeside
    </div>

    <div class="divider" style="top:476px"></div>
    <div class="icon-row" style="top:465px">
      <svg class="icon" viewBox="0 0 24 24" aria-label="Email">
        <circle cx="12" cy="12" r="12" fill="var(--green)"/>
        <rect x="6" y="8" width="12" height="8" fill="none" stroke="var(--navy)" stroke-width="1.6"/>
        <path d="M6 8l6 5 6-5" fill="none" stroke="var(--navy)" stroke-width="1.6"/>
      </svg>
      <svg class="icon" viewBox="0 0 24 24" aria-label="Website">
        <circle cx="12" cy="12" r="12" fill="var(--green)"/>
        <circle cx="12" cy="12" r="6.5" fill="none" stroke="var(--navy)" stroke-width="1.5"/>
        <path d="M5.5 12h13M12 5.5c-3 3.5-3 9.5 0 13M12 5.5c3 3.5 3 9.5 0 13" fill="none" stroke="var(--navy)" stroke-width="1.3"/>
      </svg>
    </div>
    <div class="contact" style="top:494px">
      info@lumvexholdings.com<br>
      www.lumvexholdings.com
    </div>

    <div class="divider" style="top:551px"></div>
    <div class="icon-row" style="top:540px">
      <svg class="icon" viewBox="0 0 24 24" aria-label="Location">
        <circle cx="12" cy="12" r="12" fill="var(--green)"/>
        <path d="M12 5a4.5 4.5 0 0 1 4.5 4.5C16.5 13 12 19 12 19s-4.5-6-4.5-9.5A4.5 4.5 0 0 1 12 5z" fill="var(--navy)"/>
        <circle cx="12" cy="9.5" r="1.7" fill="var(--green)"/>
      </svg>
    </div>
    <div class="contact contact--offices" style="top:569px">Offices in Harborview, Northgate and Lakeside</div>
  </section>

  <section class="card card--back" aria-label="Business card back">
    <div class="back-url">www.lumvexholdings.com</div>
    <div class="wordmark wordmark--back">
      <span class="wordmark__dot"></span><span>LUMVEX HOLDINGS</span>
    </div>
  </section>

</main>
</body>
</html>
```